Catalog for our Gold Coins for high value market

We need someone who makes our catalog or book for the gold coins of Switzerland.
Please use the Word Document. The text and the images are below. Feel free to make a nice design. Also make a nice design as a title.
Please use Adobe Indesign or Illustrator to make the content adjustable for us if needed.

You could also add a "star rating" from 1-4 for some of the coins with an image. I will do the rating later. It should be a rating of how precious the coins are without entering a price.
You could also adjust the title design with the coins.

Please make at least the following pages:
Title
Table of content
Title Page for each Ares (Aargau Page 6, Appenzell Page 6, Basel Page 8 and so on)
Pages with the content (Coins including the description)

Target Market(s)

Gold coins collectors. Usually those people are rich men.

Requirements
Must have
• Modern design
Should not have
• Not too many colors used. It should be modern. But have some class.

```html
<!DOCTYPE html>
<html lang="de">
<head>
<meta charset="utf-8">
<title>Goldmünzen der Kantone und Eidgenossenschaft – Katalog</title>
<link rel="stylesheet" href="https://fonts.googleapis.com/css2?family=Montserrat:wght@500;600;700&family=Hind:wght@400;500&display=swap">
<style>
  :root{
    --bg:#d9d9d9;
    --paper:#ffffff;
    --paper-soft:#f3f3f3;
    --ink:#222226;
    --ink-soft:#4a4a4f;
    --slate:#2c2c2f;
    --gold:#f0c020;
    --gold-deep:#c79a1c;
    --rule:#3a3a3e;
  }
  *{box-sizing:border-box;margin:0;padding:0}
  html,body{width:1200px;height:900px;overflow:hidden}
  body{background:var(--bg);font-family:"Hind",sans-serif;color:var(--ink);position:relative}

  .page{position:absolute;background:var(--paper);overflow:hidden}
  .spread{position:absolute;display:flex;box-shadow:0 6px 14px rgba(0,0,0,.12)}
  .spread .page{position:relative}
  .page--left{background:linear-gradient(to left,#e2e2e2 0,var(--paper-soft) 18px,var(--paper) 60px)}
  .page--right{background:linear-gradient(to right,#e6e6e6 0,var(--paper-soft) 14px,var(--paper) 50px)}

  /* Cover */
  .cover{left:47px;top:71px;width:355px;height:355px;box-shadow:0 6px 14px rgba(0,0,0,.14)}
  .cover__title{position:absolute;left:38px;top:45px;font-family:"Montserrat",sans-serif;font-weight:700;font-size:19px;letter-spacing:2.4px;color:var(--gold)}
  .cover__subtitle{position:absolute;left:39px;top:70px;font-family:"Montserrat",sans-serif;font-weight:500;font-size:9.2px;letter-spacing:.5px;color:var(--ink)}
  .cover__photo{position:absolute;left:0;top:86px;width:355px;height:226px;
    background:radial-gradient(ellipse 40% 55% at 24% 50%,rgba(214,170,60,.55),transparent 70%),
               radial-gradient(ellipse 30% 45% at 85% 60%,rgba(20,20,20,.6),transparent 70%),var(--slate)}
  .cover__brand{position:absolute;left:0;right:0;top:326px;display:flex;justify-content:center;align-items:center;gap:5px;
    font-family:"Hind",sans-serif;font-weight:500;font-size:11px;letter-spacing:.6px;color:var(--ink)}
  .cover__brand-mark{width:7px;height:7px;background:var(--gold)}

  /* Blank dark page */
  .page--ink{background:var(--slate)}

  /* Contents */
  .toc__heading{position:absolute;left:36px;top:34px;font-family:"Montserrat",sans-serif;font-weight:700;font-size:10.5px;letter-spacing:1.4px}
  .toc{position:absolute;left:85px;top:60px;width:163px}
  .toc__group{border-bottom:0.8px solid var(--rule);padding-bottom:6px;margin-bottom:9px}
  .toc__row{display:flex;justify-content:space-between;font-size:5.4px;line-height:9.9px;color:var(--ink-soft)}
  .toc__row--head{font-weight:500;color:var(--ink);text-transform:uppercase}

  /* Canton pages */
  .canton__name{position:absolute;font-family:"Montserrat",sans-serif;font-weight:700;font-size:19px;letter-spacing:1.6px;color:var(--ink)}
  .canton__sub{position:absolute;font-family:"Montserrat",sans-serif;font-weight:700;font-size:10.6px;letter-spacing:.6px;color:var(--ink)}
  .canton__text{position:absolute;left:36px;top:88px;width:260px;font-size:5.6px;line-height:9px;color:var(--ink-soft)}
  .coin-photo{position:absolute}
  .coin-photo--dark{background:radial-gradient(ellipse 30% 55% at 30% 50%,rgba(214,168,52,.85),transparent 75%),
                                radial-gradient(ellipse 30% 55% at 70% 50%,rgba(214,168,52,.85),transparent 75%),var(--slate)}
  .coin-photo--light{background:radial-gradient(ellipse 24% 50% at 25% 50%,rgba(222,182,80,.9),transparent 78%),
                                 radial-gradient(ellipse 24% 50% at 75% 50%,rgba(222,182,80,.9),transparent 78%),transparent}
  .coin-photo--stack{border:0.8px solid #9a9a9a;border-left:none;
    background:radial-gradient(ellipse 30% 20% at 58% 25%,rgba(222,182,80,.9),transparent 78%),
               radial-gradient(ellipse 30% 20% at 58% 72%,rgba(222,182,80,.9),transparent 78%),var(--paper)}
  .coin-caption{position:absolute;font-family:"Montserrat",sans-serif;font-weight:700;font-size:6.1px;letter-spacing:.4px;text-align:center;white-space:nowrap;transform:translateX(-50%)}
  .rating{position:absolute;transform:translateX(-50%)}
  .page-no{position:absolute;top:337px;font-size:4.8px;color:var(--ink-soft)}
  .page-no b{font-weight:500;color:var(--ink)}
</style>
</head>
<body>

<svg width="0" height="0" style="position:absolute" aria-hidden="true">
  <defs>
    <symbol id="star" viewBox="0 0 20 20"><path d="M10 1.5l2.6 5.6 6.1.7-4.5 4.2 1.2 6L10 15l-5.4 3 1.2-6L1.3 7.8l6.1-.7z"/></symbol>
    <linearGradient id="half"><stop offset="50%" stop-color="#f0c020"/><stop offset="50%" stop-color="#fff" stop-opacity="0"/></linearGradient>
  </defs>
</svg>

<!-- Cover -->
<section class="page cover" aria-label="Titelseite">
  <h1 class="cover__title">GOLDMÜNZEN</h1>
  <p class="cover__subtitle">der Kantone und Eidgenossenschaft</p>
  <div class="cover__photo" role="img" aria-label="Foto: Schweizer Goldmünzen, Lupe, Sukkulente und Lederetui mit Stift auf dunklem Grund"></div>
  <div class="cover__brand"><span class="cover__brand-mark"></span>Aurum Kessler</div>
</section>

<!-- Spread: contents -->
<section class="spread" style="left:473px;top:71px" aria-label="Inhaltsverzeichnis">
  <div class="page page--ink" style="width:331px;height:355px"></div>
  <div class="page page--right" style="width:331px;height:355px">
    <h2 class="toc__heading">INHALT</h2>
    <div class="toc">
      <div class="toc__group">
        <div class="toc__row toc__row--head"><span>Aargau</span><span>6</span></div>
        <div class="toc__row"><span>Abt Benedikt von Hallau 1684 – 1723</span><span>6</span></div>
      </div>
      <div class="toc__group">
        <div class="toc__row toc__row--head"><span>Appenzell</span><span>7</span></div>
        <div class="toc__row"><span>Appenzell Innerrhoden</span><span>7</span></div>
      </div>
      <div class="toc__group">
        <div class="toc__row toc__row--head"><span>Basel</span><span>8</span></div>
        <div class="toc__row"><span>Reichsmünzstätte</span><span>8</span></div>
        <div class="toc__row"><span>Reichsmünzstätte 15. Jahrhundert</span><span>8</span></div>
        <div class="toc__row"><span>Stadt Basel 16. Jahrhundert</span><span>13</span></div>
        <div class="toc__row"><span>Stadt Basel 17. Jahrhundert</span><span>14</span></div>
        <div class="toc__row"><span>Stadt Basel 18. Jahrhundert</span><span>16</span></div>
        <div class="toc__row"><span>Bistum Basel</span><span>19</span></div>
        <div class="toc__row"><span>Johann Franz von Lindegg 1651 -1656</span><span>19</span></div>
        <div class="toc__row"><span>Johann Konrad I. von Ebersbach 1656-1693</span><span>19</span></div>
        <div class="toc__row"><span>Johann Konrad II. von Tannegg-Wilbach 1705-1737</span><span>19</span></div>
      </div>
      <div class="toc__group">
        <div class="toc__row toc__row--head"><span>Bern</span><span>20</span></div>
        <div class="toc__row"><span>Bern – 15. Jahrhundert</span><span>20</span></div>
        <div class="toc__row"><span>Bern – 16. Jahrhundert</span><span>20</span></div>
        <div class="toc__row"><span>Bern – 17. Jahrhundert</span><span>22</span></div>
        <div class="toc__row"><span>Bern – 18. Jahrhundert</span><span>26</span></div>
        <div class="toc__row"><span>Bern – 19. Jahrhundert</span><span>47</span></div>
      </div>
    </div>
    <p class="page-no" style="left:306px">Page <b>1</b></p>
  </div>
</section>

<!-- Spread: Aargau / Appenzell -->
<section class="spread" style="left:473px;top:472px" aria-label="Kantone Aargau und Appenzell">
  <div class="page page--left" style="width:331px;height:355px">
    <h2 class="canton__name" style="left:36px;top:34px">AARGAU</h2>
    <h3 class="canton__sub" style="left:36px;top:64px">ABT BENEDIKT VON HALLAU 1684 – 1723</h3>
    <p class="canton__text">Benedikt von Hallau (* 13. August 1646 in Bremgarten; † 14. September 1723 auf Schloss Sandegg) war ein Schweizer Benediktinermönch. Von 1684 bis 1701 war er Abt, danach bis zu seinem Tod erster Fürstabt des Klosters Muri in den Freien Ämtern (im heutigen Kanton Aargau).</p>
    <div class="coin-photo coin-photo--dark" style="left:0;top:121px;width:186px;height:88px" role="img" aria-label="Foto: 5 Dukaten 1720, Vorder- und Rückseite auf dunklem Grund"></div>
    <p class="coin-caption" style="left:94px;top:216px">5 DUKATEN (JAHR 1720, HMZ 2-11A)</p>
    <svg class="rating" style="left:94px;top:229px" width="55" height="10" viewBox="0 0 55 10" aria-label="4,5 von 5 Sternen">
      <g fill="var(--gold)"><use href="#star" x="0" width="10" height="10"/><use href="#star" x="11" width="10" height="10"/><use href="#star" x="22" width="10" height="10"/><use href="#star" x="33" width="10" height="10"/></g>
      <use href="#star" x="44" width="10" height="10" fill="url(#half)" stroke="var(--gold)" stroke-width="1.2"/>
    </svg>
    <div class="coin-photo coin-photo--light" style="left:154px;top:235px;width:142px;height:71px" role="img" aria-label="Foto: Dukat 1720, Vorderseite mit Bildnis und Rückseite mit Wappen"></div>
    <p class="coin-caption" style="left:225px;top:314px">DUKAT (JAHR 1720, HMZ 2-12A)</p>
    <svg class="rating" style="left:225px;top:327px" width="55" height="10" viewBox="0 0 55 10" aria-label="5 von 5 Sternen">
      <g fill="var(--gold)"><use href="#star" x="0" width="10" height="10"/><use href="#star" x="11" width="10" height="10"/><use href="#star" x="22" width="10" height="10"/><use href="#star" x="33" width="10" height="10"/><use href="#star" x="44" width="10" height="10"/></g>
    </svg>
    <p class="page-no" style="left:11px">Page <b>6</b></p>
  </div>
  <div class="page page--right" style="width:331px;height:355px">
    <h2 class="canton__name" style="left:135px;top:34px">APPENZELL</h2>
    <h3 class="canton__sub" style="left:135px;top:64px">APPENZELL INNERRHODEN</h3>
    <div class="coin-photo coin-photo--stack" style="left:0;top:86px;width:119px;height:168px" role="img" aria-label="Foto: Dukat 1739, Vorder- und Rückseite übereinander"></div>
    <p class="coin-caption" style="left:68px;top:263px">DUKAT (JAHR 1739, HMZ 2-35B)</p>
    <svg class="rating" style="left:68px;top:276px" width="55" height="10" viewBox="0 0 55 10" aria-label="4 von 5 Sternen">
      <g fill="var(--gold)"><use href="#star" x="0" width="10" height="10"/><use href="#star" x="11" width="10" height="10"/><use href="#star" x="22" width="10" height="10"/><use href="#star" x="33" width="10" height="10"/></g>
      <use href="#star" x="44" width="10" height="10" fill="none" stroke="var(--gold)" stroke-width="1.2"/>
    </svg>
    <div class="coin-photo coin-photo--dark" style="left:144px;top:183px;width:187px;height:122px" role="img" aria-label="Foto: Dukat 1737, Vorder- und Rückseite auf dunklem Grund"></div>
    <p class="coin-caption" style="left:226px;top:313px">DUKAT (JAHR 1737, HMZ 2-35A)</p>
    <svg class="rating" style="left:226px;top:326px" width="55" height="10" viewBox="0 0 55 10" aria-label="4,5 von 5 Sternen">
      <g fill="var(--gold)"><use href="#star" x="0" width="10" height="10"/><use href="#star" x="11" width="10" height="10"/><use href="#star" x="22" width="10" height="10"/><use href="#star" x="33" width="10" height="10"/></g>
      <use href="#star" x="44" width="10" height="10" fill="url(#half)" stroke="var(--gold)" stroke-width="1.2"/>
    </svg>
    <p class="page-no" style="left:306px">Page <b>7</b></p>
  </div>
</section>

</body>
</html>
```